Diverse business needs a corporate identity system

Brantow Fielding Holdings Limited is a well established family owned and run business operating in Port Moresby, Papua New Guinea since 1989. As part of taking the business to the next level, we are redoing our branding/corporate identity.

We currently carry out two core business activities servicing corporate clients in the commercial and industrial sectors:
1. Electrical - new installations and maintenance work
2. Construction - mostly commercial & industrial, some residential

We are looking to add the following business activities in near future:
1. IT consulting
2. Property development - business/industrial park, residential complexes, low cost housing
3. Retail of hardware, construction supplies and flat pack furniture & kitchens

We have just completed our logo design here on SketchHarbor and now wanting to design business card and stationery based on our new logo (attached).

Deliverables are:
1. Business card - double sided
2. Letterhead A4

Details to go on the card:
Name: Marcus Trevane
Title: Director
Email: marcus.trevane@brantowfield.com
Tel: +675 3147720, +675 3148815
Office: Section 17 Lot 48, Waravu Light Industrial Area, Port Moresby, Papua New Guinea
Postal: PO Box 419, Waravu, NCD, Papua New Guinea
Website: brantowfield.com

Our services can be listed somewhere on the card:
Electrical, Construction, Property Development, IT Consulting

Details to go on the letterhead:
Brantow Fielding Holdings Ltd.
PO Box 419, Waravu, NCD, Papua New Guinea
Fax: +675 3146603
Email: info@brantowfield.com

For inspiration, I have uploaded some images of business cards we like.

Would be good if the same/similar business card design could be printed both economically (e.g. full coloured both sides, matte card stock) for majority of staff and upscaled to use premium features such as letter pressed, foil etc for use by executives. Otherwise, please provide two separate designs.

Logo text font is nexa bold freefont - please use something from nexa family or another font type that complements it.

Reason: Few designs were submitted. Most were clearly from ready to use templates. No designs really stand out for us at the moment. So we have decided to narrow the focus to just business card and A4 letterhead. And also revised the brief to be completely open to hopefully invite more creative designs.

I have updated the brief to be a lot less restrictive to try and get more creative designs. Also uploaded more images of premium business cards for inspiration.

Industry/Entity Type

Construction

Requirements
Must have
• All designs must conform to printolane specifications. Refer to and download appropriate work file templates from http://www.printolane.com.au/pl/ns/files/UploadResources.aspx?GP=1%2F9%2F2014+12%3A53%3A21+AM&GPS=5829104463&GNF=1&selectedTab=0.
Should not have
• No QR codes and social media links.

```html
<!DOCTYPE html>
<html lang="en">
<head>
<meta charset="utf-8">
<title>Brantow Fielding – Business Card</title>
<link rel="stylesheet" href="https://fonts.googleapis.com/css2?family=Quicksand:wght@500;700&display=swap">
<style>
  :root {
    --page-bg: #d9d6d1;
    --card-dark: #262626;
    --card-light: #efefef;
    --brand-red: #d8362a;
    --text-grey: #4a4a4a;
    --text-white: #f2f2f2;
  }
  * { box-sizing: border-box; margin: 0; padding: 0; }
  html, body {
    width: 1200px; height: 900px; overflow: hidden;
    background: var(--page-bg);
    font-family: "Quicksand", sans-serif;
  }
  .sheet {
    width: 1200px; height: 900px;
    display: flex; flex-direction: column;
    align-items: center; justify-content: center; gap: 56px;
  }
  .card {
    position: relative;
    width: 600px; height: 350px;
    overflow: hidden;
    box-shadow: 0 6px 18px rgba(0,0,0,0.18);
  }

  /* Front */
  .card-front { background: var(--card-dark); }
  .card-front .brand {
    position: absolute; left: 0; right: 0; top: 118px;
    display: flex; align-items: center; justify-content: center; gap: 14px;
    padding-left: 60px;
  }
  .card-front .brand-dot {
    width: 40px; height: 40px; border-radius: 50%;
    background: var(--brand-red); flex: none;
  }
  .card-front .brand-name {
    color: var(--brand-red);
    font-weight: 700; font-size: 30px; line-height: 1;
    white-space: nowrap;
  }
  .card-front .website {
    position: absolute; left: 60px; bottom: 70px;
    color: var(--text-white);
    font-weight: 500; font-size: 15px; letter-spacing: 4px;
  }

  /* Back */
  .card-back { background: var(--card-light); }
  .card-back .brand {
    position: absolute; left: 34px; top: 122px;
    display: flex; align-items: center; gap: 8px;
  }
  .card-back .brand-dot {
    width: 22px; height: 22px; border-radius: 50%;
    background: var(--brand-red); flex: none;
  }
  .card-back .brand-name {
    color: var(--brand-red);
    font-weight: 700; font-size: 22px; line-height: 1;
    white-space: nowrap;
  }
  .details {
    position: absolute; left: 318px; top: 58px;
    color: var(--text-grey);
    font-weight: 500; font-size: 14px; line-height: 1.3;
  }
  .person-name {
    color: var(--brand-red);
    font-weight: 700; font-size: 15px; text-transform: uppercase;
    letter-spacing: 0.2px;
  }
  .person-title { margin-bottom: 10px; }
  .contact-line { display: flex; align-items: center; gap: 8px; white-space: nowrap; }
  .contact-line svg { width: 11px; height: 11px; fill: var(--brand-red); flex: none; }
  .address { margin-top: 18px; }
  .postal { margin-top: 14px; }
</style>
</head>
<body>
<main class="sheet">

  <section class="card card-front" aria-label="Business card front">
    <div class="brand">
      <span class="brand-dot"></span>
      <span class="brand-name">Brantow Fielding</span>
    </div>
    <p class="website">www.brantowfield.com</p>
  </section>

  <section class="card card-back" aria-label="Business card back">
    <div class="brand">
      <span class="brand-dot"></span>
      <span class="brand-name">Brantow Fielding</span>
    </div>

    <div class="details">
      <p class="person-name">Marcus Trevane</p>
      <p class="person-title">Director</p>
      <p class="contact-line">
        <svg viewBox="0 0 12 12" aria-hidden="true"><rect x="3" y="0.5" width="6" height="11" rx="1.2"/></svg>
        +675 31 47 720
      </p>
      <p class="contact-line">
        <svg viewBox="0 0 12 12" aria-hidden="true"><path d="M0 2h12v8H0z M0 2l6 4.5L12 2"/></svg>
        marcus.trevane@brantowfield.com
      </p>
      <p class="address">Section 17 Lot 48,<br>Waravu Light Industrial Area,<br>Port Moresby, Papua New Guinea</p>
      <p class="postal">PO Box 419, Waravu,<br>NCD, Papua New Guinea</p>
    </div>
  </section>

</main>
</body>
</html>
```